Clearbrook Lawnworks LLC Business Card

Ok, first off let me thank you for taking the time to participate in this project !! I have my business logo that I want incorporated into business card design . My irrigation business is located in a very upscale part of town and we do high end homes . So with that said I'm planning on these cards being plastic credit card type cards. I would like them to be two sided . I'm thinking something bold , yet classy and clean . Not too busy . We do different types of work . 80% irrigation service and installation . 15% landscape lighting and the other 5% drainage and hardscapes ! I have a website that I want listed on it as well as our address , phone number and of course my name and title .

Target Market(s)

Upscale homeowners and architects

Industry/Entity Type

Landscape

Requirements
Must have
• Company logo, website, address , phone number , name , title , services offered

Www.ClearbrookLawnworks.example
Marcus Hendley owner
205-555-0148
Clearbrook Lawnworks LLC
P.O. Box 478512
Millbrook Falls, Alabama 35090

```html
<!DOCTYPE html>
<html lang="en">
<head>
<meta charset="utf-8">
<title>Clearbrook Lawnworks LLC – Business Card</title>
<link href="https://fonts.googleapis.com/css2?family=PT+Sans:ital,wght@0,400;0,700;1,400;1,700&display=swap" rel="stylesheet">
<style>
  :root {
    --page-bg: #eeeeec;
    --card-white: #ffffff;
    --brand-blue: #0a9ad8;
    --deep-blue: #1f4f9c;
    --leaf-green: #6cb33f;
    --ink: #111111;
    --on-blue: #ffffff;
  }
  * { box-sizing: border-box; margin: 0; padding: 0; }
  html, body { width: 1200px; height: 999px; overflow: hidden; }
  body {
    background: var(--page-bg);
    font-family: "PT Sans", "Helvetica Neue", Arial, sans-serif;
    position: relative;
  }
  .card {
    position: absolute;
    width: 508px;
    height: 290px;
    background: var(--card-white);
    box-shadow: 0 2px 8px rgba(0,0,0,0.18);
    overflow: hidden;
  }
  /* Front side */
  .card-front { left: 225px; top: 190px; }
  .front-brand {
    position: absolute;
    left: 0; right: 0; top: 70px;
    display: flex; flex-direction: column; align-items: center;
  }
  .brand-dot {
    width: 84px; height: 84px; border-radius: 50%;
    background: var(--brand-blue);
    margin-bottom: 14px;
  }
  .brand-name {
    color: var(--leaf-green);
    font-weight: 700;
    font-size: 38px;
    line-height: 1;
  }
  .front-web {
    position: absolute; left: 0; right: 0; top: 222px;
    text-align: center;
    color: var(--brand-blue);
    font-size: 22px;
  }
  /* Back side */
  .card-back { left: 503px; top: 524px; width: 507px; height: 288px; }
  .back-panel { position: absolute; inset: 0; }
  .holder {
    position: absolute; left: 33px; top: 34px;
    font-style: italic; color: var(--ink);
  }
  .holder-name { font-weight: 700; font-size: 18px; line-height: 1.1; }
  .holder-title { font-size: 14px; }
  .address {
    position: absolute; left: 33px; top: 147px;
    color: var(--on-blue); font-style: italic; font-weight: 700;
    font-size: 13px; line-height: 1.4;
  }
  .contact {
    position: absolute; left: 33px; top: 220px;
    color: var(--on-blue); font-style: italic; font-weight: 700;
  }
  .contact-row { display: flex; align-items: center; gap: 5px; }
  .contact-phone { font-size: 18px; }
  .contact-web { font-size: 12.5px; margin-top: 1px; }
  .contact svg { flex: none; }
  .back-brand {
    position: absolute; left: 215px; width: 265px; top: 36px;
    display: flex; flex-direction: column; align-items: center;
  }
  .back-brand .brand-dot { width: 70px; height: 70px; margin-bottom: 12px; }
  .back-brand .brand-name { font-size: 25px; }
  .services {
    position: absolute; right: 30px; top: 181px;
    text-align: right; font-style: italic; font-weight: 700;
    font-size: 14.5px; line-height: 1.38; color: var(--ink);
  }
  .services-heading { color: var(--brand-blue); font-size: 15px; }
  .services li { list-style: none; }
  .services li::before { content: "• "; color: var(--brand-blue); }
</style>
</head>
<body>

  <section class="card card-front" aria-label="Card front">
    <div class="front-brand">
      <span class="brand-dot" aria-hidden="true"></span>
      <span class="brand-name">Clearbrook Lawnworks</span>
    </div>
    <p class="front-web">www.clearbrooklawnworks.example</p>
  </section>

  <section class="card card-back" aria-label="Card back">
    <svg class="back-panel" width="507" height="288" viewBox="0 0 507 288" aria-hidden="true">
      <defs>
        <linearGradient id="panelFade" x1="0" y1="0" x2="0" y2="1">
          <stop offset="0" stop-color="#ffffff"/>
          <stop offset="0.12" stop-color="#d8eefa"/>
          <stop offset="0.3" stop-color="#f4fbff"/>
          <stop offset="0.42" stop-color="#0a9ad8"/>
          <stop offset="0.7" stop-color="#1c69b5"/>
          <stop offset="1" stop-color="#1f4f9c"/>
        </linearGradient>
      </defs>
      <path d="M0 0 H200 C165 60 185 200 312 288 H0 Z" fill="url(#panelFade)"/>
    </svg>

    <div class="holder">
      <p class="holder-name">Marcus Hendley</p>
      <p class="holder-title">Owner</p>
    </div>

    <p class="address">P.O. Box 478512<br>Millbrook Falls<br>Alabama 35090</p>

    <div class="contact">
      <p class="contact-row contact-phone">
        <svg width="17" height="11" viewBox="0 0 17 11" aria-hidden="true"><path d="M1 5 C1 1 16 1 16 5 L13 6 L11 4 H6 L4 6 Z M5 6 H12 L14 10 H3 Z" fill="#fff"/></svg>
        205-555-0148
      </p>
      <p class="contact-row contact-web">
        <svg width="14" height="14" viewBox="0 0 14 14" aria-hidden="true" fill="none" stroke="#fff" stroke-width="1.2"><circle cx="7" cy="7" r="6"/><ellipse cx="7" cy="7" rx="2.6" ry="6"/><path d="M1 7 H13 M2 4 H12 M2 10 H12"/></svg>
        www.clearbrooklawnworks.example
      </p>
    </div>

    <div class="back-brand">
      <span class="brand-dot" aria-hidden="true"></span>
      <span class="brand-name">Clearbrook Lawnworks</span>
    </div>

    <div class="services">
      <p class="services-heading">Services Offered:</p>
      <ul>
        <li>Irrigation Service &amp; Installation</li>
        <li>Landscape Lighting</li>
        <li>Drainage &amp; Hardscapes</li>
      </ul>
    </div>
  </section>

</body>
</html>
```